Full Truck Wrap for residential and commercial roofing company

I am looking to get my trucks wrapped to help build brand in newer markets that aren't growing as fast as we would like due to branding not popping out as much as we like! We are a roofing company who provides roofing services to residential and commercial property owners in Alabama & Georgia in the united states. Our main services are storm restoration, roofing, gutters, siding, assisting clients in insurance claims to restore their properties after a loss due to severe storms.

My goal with this truck wrap is to generate a truck wrap we can use for the next 5-10 years on several different types of vehicles and job trailers. I would like to keep the design simple yet, professional, modern, easy to read, and rememberable. We want to have the rear window wrapped as well to provide information to people sitting behind us in traffic or sees our vehicles parked somewhere. Information on rear window needs to have Sales Rep first and last name, phone number, company website, and etc.

I will attach a few example of wraps that I liked and thought looked good to me and was something we could easily use for years to come. Please submit any ideas you have for review as i am open to any recommendations for this wrap, providing this information as a starting point. Attached are 2 different logos we have, don't want both logos on same design only providing them both incase a design looks better with the other. I also added some side shots of the trucks needing wraps incase you are able to provided a proof with that so we can see it on the first truck getting wrapped.
Updates

still looking for a design for this contest, nothing has really been what i was expecting. please upload more if you have more design recommendations

Target Market(s)

Higher in residential properties and business owners with properties

Industry/Entity Type

Roofing Company, residential and commercial construction

Font styles to use
Sans Serif

Requirements
Nice to have
• Modern design that is more of a corporation look. We will be wrapping our entire fleet with this new wrap design.
Should not have
• Similar designs to generic wrap designs

```html
<!DOCTYPE html>
<html lang="en">
<head>
<meta charset="utf-8">
<title>Summit Crest Roofing – Vehicle Wrap Side Panel</title>
<link rel="stylesheet" href="https://fonts.googleapis.com/css2?family=Montserrat:wght@700;800;900&family=Open+Sans:wght@600;700&display=swap">
<style>
  :root {
    --wrap-red: #e0060f;
    --wrap-black: #141414;
    --wrap-white: #ffffff;
    --ink: #1b1b1b;
    --pixel-grey: #d4d4d4;
    --backdrop: #eeeeee;
  }
  * { box-sizing: border-box; margin: 0; padding: 0; }
  html, body {
    width: 1200px;
    height: 760px;
    overflow: hidden;
    background: var(--backdrop);
  }
  .canvas {
    position: relative;
    width: 1200px;
    height: 760px;
  }
  .wrap-panel {
    position: absolute;
    left: 50px;
    top: 160px;
    width: 1100px;
    height: 440px;
    background: var(--wrap-white);
    box-shadow: 0 2px 10px rgba(0,0,0,0.08);
    overflow: hidden;
  }
  .wrap-graphics {
    position: absolute;
    inset: 0;
    width: 1100px;
    height: 440px;
  }
  .brand-name {
    position: absolute;
    left: 40px;
    top: 150px;
    width: 440px;
    font-family: "Montserrat", sans-serif;
    font-weight: 900;
    color: var(--ink);
    line-height: 1;
    text-align: center;
  }
  .brand-name .brand-line {
    display: block;
    font-size: 58px;
    letter-spacing: 0.5px;
  }
  .brand-name .brand-sub {
    display: block;
    font-size: 30px;
    letter-spacing: 6px;
    margin-top: 14px;
  }
  .website {
    position: absolute;
    right: 34px;
    top: 74px;
    font-family: "Montserrat", sans-serif;
    font-weight: 800;
    font-size: 38px;
    letter-spacing: 2px;
    color: var(--wrap-white);
  }
  .phone {
    position: absolute;
    left: 790px;
    top: 208px;
    display: flex;
    align-items: center;
    gap: 10px;
    font-family: "Open Sans", sans-serif;
    font-weight: 700;
    font-size: 30px;
    color: var(--wrap-white);
  }
  .phone-icon { width: 30px; height: 30px; }
  .service-area {
    position: absolute;
    left: 790px;
    top: 290px;
    font-family: "Open Sans", sans-serif;
    font-weight: 600;
    font-size: 30px;
    line-height: 1.2;
    color: var(--ink);
  }
  .service-area .state-second { display: block; padding-left: 52px; }
</style>
</head>
<body>
<main class="canvas">
  <section class="wrap-panel" aria-label="Vehicle wrap side panel">
    <svg class="wrap-graphics" viewBox="0 0 1100 440" aria-hidden="true">
      <polygon class="accent-band" points="500,0 545,0 745,200 1100,200 1100,262 722,262" fill="var(--wrap-red)"/>
      <polygon class="dark-field" points="545,0 1100,0 1100,200 745,200" fill="var(--wrap-black)"/>
      <g class="pixel-squares" fill="var(--pixel-grey)">
        <rect x="750" y="350" width="10" height="10"/>
        <rect x="763" y="350" width="10" height="10"/>
        <rect x="750" y="363" width="10" height="10"/>
        <rect x="763" y="363" width="10" height="10"/>
        <rect x="985" y="295" width="10" height="10"/>
        <rect x="985" y="318" width="10" height="10"/>
        <rect x="1040" y="318" width="12" height="12"/>
        <rect x="1055" y="318" width="12" height="12"/>
        <rect x="1040" y="333" width="12" height="12"/>
        <rect x="1055" y="333" width="12" height="12"/>
        <rect x="1010" y="370" width="8" height="8"/>
        <rect x="1021" y="370" width="8" height="8"/>
      </g>
    </svg>

    <h1 class="brand-name">
      <span class="brand-line">SUMMIT CREST</span>
      <span class="brand-sub">ROOFING</span>
    </h1>

    <p class="website">WWW.SUMMITCRESTGA.COM</p>

    <p class="phone">
      <svg class="phone-icon" viewBox="0 0 24 24" aria-hidden="true">
        <circle cx="12" cy="12" r="11" fill="var(--wrap-white)"/>
        <path d="M8.2 6.5l1.8-.4 1.2 2.8-1.3 1c.6 1.4 1.7 2.5 3.1 3.1l1-1.3 2.8 1.2-.4 1.8c-.2.6-.8 1-1.4.9C11.3 15 9 12.7 8.3 7.9c-.1-.6.3-1.2.9-1.4z" fill="var(--wrap-red)"/>
      </svg>
      (555) 014-2290
    </p>

    <p class="service-area">Alabama &amp;<span class="state-second">Georgia</span></p>
  </section>
</main>
</body>
</html>
```